Business Card Design Project

Business card for new event planning company. I will load in 2 different colors of logs for you to use.

Target Market(s)

meeting planners and business leaders

Industry/Entity Type

Event Planning

Requirements
Must have
• memorable/ creative please - maybe logo on back of the card

Information for business card: (Information may change)

LaVonna Pettibrook
lav@MarigoldOccasionsandGalas.com
www.MarigoldOccasionsandGalas.com
613.275.9042
Nice to have
• Do you think it would be too much to add chirpy, QX, workmesh logo to card to connect?

all are LaVonna Pettibrook

```html
<!DOCTYPE html>
<html lang="en">
<head>
<meta charset="utf-8">
<title>Marigold Occasions &amp; Galas — Business Card</title>
<link rel="stylesheet" href="https://fonts.googleapis.com/css2?family=Roboto+Condensed:wght@400;700&display=swap">
<style>
  :root {
    --backdrop: #e4e4e6;
    --card-white: #ffffff;
    --brand-purple: #7b62b8;
    --brand-red: #d8312a;
    --red-light: #d42a22;
    --red-deep: #9e1010;
    --motif: rgba(232, 70, 58, 0.55);
    --text-light: #ffffff;
    --shadow: rgba(0, 0, 0, 0.18);
  }
  * { box-sizing: border-box; margin: 0; padding: 0; }
  html, body {
    width: 1200px;
    height: 775px;
    overflow: hidden;
    background: var(--backdrop);
    font-family: "Roboto Condensed", "Arial Narrow", sans-serif;
  }
  .stage {
    width: 1200px;
    height: 775px;
    display: flex;
    align-items: center;
    justify-content: center;
    gap: 40px;
  }
  .card {
    position: relative;
    width: 540px;
    height: 309px;
    border-radius: 4px;
    overflow: hidden;
    box-shadow: 0 10px 28px var(--shadow);
  }

  /* Front */
  .card--front {
    background: var(--card-white);
    display: flex;
    flex-direction: column;
    align-items: center;
    justify-content: center;
  }
  .brand-mark {
    display: flex;
    align-items: center;
    gap: 14px;
    color: var(--brand-purple);
    font-weight: 400;
  }
  .brand-mark__dot {
    width: 22px;
    height: 22px;
    border-radius: 50%;
    background: var(--brand-purple);
  }
  .brand-mark__name { display: flex; flex-direction: column; line-height: 1; }
  .brand-mark__word { font-size: 64px; }
  .brand-mark__sub { font-size: 19px; margin-top: 4px; letter-spacing: 0.5px; }
  .front-url {
    margin-top: 46px;
    color: var(--brand-red);
    font-size: 17px;
    font-weight: 700;
    letter-spacing: 2.4px;
  }

  /* Back */
  .card--back {
    background: radial-gradient(ellipse at 60% 40%, var(--red-light) 0%, var(--red-deep) 100%);
    color: var(--text-light);
  }
  .back-motif {
    position: absolute;
    right: 40px;
    top: 30px;
    width: 150px;
    height: 230px;
    border-radius: 70px 70px 40px 40px;
    background: radial-gradient(ellipse at 50% 45%, var(--motif) 0%, rgba(232, 70, 58, 0.15) 80%, transparent 100%);
  }
  .back-content {
    position: absolute;
    left: 36px;
    top: 46px;
  }
  .back-brand {
    display: flex;
    align-items: center;
    gap: 10px;
    font-weight: 400;
    color: var(--text-light);
  }
  .back-brand__dot {
    width: 12px;
    height: 12px;
    border-radius: 50%;
    background: var(--text-light);
  }
  .back-brand__name { display: flex; flex-direction: column; line-height: 1; }
  .back-brand__word { font-size: 38px; }
  .back-brand__sub { font-size: 12px; margin-top: 2px; }
  .person-name {
    margin-top: 22px;
    font-size: 24px;
    font-weight: 700;
  }
  .contact-list { list-style: none; margin-top: 10px; }
  .contact-list li {
    display: flex;
    align-items: center;
    gap: 10px;
    font-size: 14px;
    line-height: 23px;
  }
  .contact-list svg { width: 13px; height: 13px; flex: none; }
  .social-row {
    display: flex;
    align-items: center;
    gap: 10px;
    margin-top: 16px;
    font-size: 12px;
  }
  .social-item { display: flex; align-items: center; gap: 4px; }
  .social-item__box {
    width: 11px;
    height: 11px;
    background: var(--text-light);
    border-radius: 2px;
  }
  .social-divider {
    width: 1px;
    height: 14px;
    background: var(--text-light);
    opacity: 0.8;
  }
</style>
</head>
<body>
<main class="stage">
  <section class="card card--front" aria-label="Card front">
    <div class="brand-mark">
      <span class="brand-mark__dot"></span>
      <div class="brand-mark__name">
        <span class="brand-mark__word">Marigold</span>
        <span class="brand-mark__sub">Occasions&amp;Galas</span>
      </div>
    </div>
    <p class="front-url">www.marigoldoccasionsandgalas.com</p>
  </section>

  <section class="card card--back" aria-label="Card back">
    <div class="back-motif" role="img" aria-label="Large faint flower motif from the brand"></div>
    <div class="back-content">
      <div class="back-brand">
        <div class="back-brand__name">
          <span class="back-brand__word">Marigold</span>
          <span class="back-brand__sub">Occasions&amp;Galas</span>
        </div>
        <span class="back-brand__dot"></span>
      </div>
      <h1 class="person-name">LaVonna Pettibrook</h1>
      <ul class="contact-list">
        <li>
          <svg viewBox="0 0 16 16" aria-hidden="true"><path fill="#fff" d="M3.6 1.2 6 3.6 4.8 5.6c.8 2 2.6 3.8 4.6 4.6l2-1.2 2.4 2.4-1.6 2.4C6.8 13.6 2.4 9.2 1.2 2.8z"/></svg>
          <span>613.275.9042</span>
        </li>
        <li>
          <svg viewBox="0 0 16 16" aria-hidden="true"><rect x="1" y="3" width="14" height="10" rx="1.5" fill="#fff"/><path d="M1.5 4 8 9l6.5-5" fill="none" stroke="#b11a16" stroke-width="1.4"/></svg>
          <span>lav@MarigoldOccasionsandGalas.com</span>
        </li>
        <li>
          <svg viewBox="0 0 16 16" aria-hidden="true"><g fill="none" stroke="#fff" stroke-width="1.3"><circle cx="8" cy="8" r="6.5"/><ellipse cx="8" cy="8" rx="3" ry="6.5"/><path d="M1.5 8h13"/></g></svg>
          <span>www.MarigoldOccasionsandGalas.com</span>
        </li>
      </ul>
      <div class="social-row">
        <span class="social-item"><span class="social-item__box"></span>QX</span>
        <span class="social-item"><span class="social-item__box"></span>chirpy</span>
        <span class="social-item"><span class="social-item__box"></span>workmesh</span>
        <span class="social-divider"></span>
        <span>LaVonna Pettibrook</span>
      </div>
    </div>
  </section>
</main>
</body>
</html>
```